Business Card Design

Electronic Security
Alarm Systems
CCTV
Electronic Access Control
Security System Integration

Industry/Entity Type

Business

Contact Information for Business Card

Declan Whitfield
PO Box 862
Carrowbrook Qld 4179
Phone 07 38265014
Mob 0428615937

```html
<!DOCTYPE html>
<html lang="en">
<head>
<meta charset="utf-8">
<title>Vantora Security – Business Card</title>
<link rel="stylesheet" href="https://fonts.googleapis.com/css2?family=Open+Sans:wght@400;600&display=swap">
<style>
  :root {
    --stage: #1f5670;
    --card: #ffffff;
    --brand-blue: #1e87a8;
    --ink: #2b2b2b;
    --rule: #3a3a3a;
    --accent-orange: #f0a056;
    --faint-blue: #cfe6f6;
    --band-text: #ffffff;
  }
  * { box-sizing: border-box; margin: 0; padding: 0; }
  html, body { width: 1200px; height: 385px; overflow: hidden; }
  body {
    background: var(--stage);
    font-family: "Open Sans", Arial, sans-serif;
    position: relative;
  }
  .card {
    position: absolute;
    top: 44px;
    width: 529px;
    height: 304px;
    background: var(--card);
    overflow: hidden;
    box-shadow: 0 3px 10px rgba(0,0,0,.35);
  }
  .card--front { left: 49px; }
  .card--back  { left: 626px; }

  .faint-square {
    position: absolute;
    width: 230px;
    height: 230px;
    background: var(--faint-blue);
    opacity: .55;
  }
  .card--front .faint-square { left: 420px; top: 20px; }
  .card--back  .faint-square { left: 380px; top: 40px; }

  .brand {
    position: absolute;
    display: flex;
    flex-direction: column;
    align-items: center;
    gap: 22px;
  }
  .card--front .brand { left: 22px; top: 50px; width: 215px; }
  .card--back  .brand { left: 115px; top: 50px; width: 300px; }
  .brand-square {
    width: 80px;
    height: 80px;
    background: var(--brand-blue);
  }
  .brand-name {
    font-size: 38px;
    font-weight: 400;
    color: var(--ink);
    letter-spacing: .5px;
    line-height: 1;
  }

  .divider {
    position: absolute;
    left: 266px;
    top: 29px;
    width: 2px;
    height: 213px;
    background: var(--rule);
  }
  .contact-name {
    position: absolute;
    left: 285px;
    top: 26px;
    font-size: 23px;
    font-weight: 600;
    color: var(--brand-blue);
  }
  .contact-title {
    position: absolute;
    left: 285px;
    top: 60px;
    font-size: 14px;
    color: var(--ink);
  }
  .services {
    position: absolute;
    left: 287px;
    top: 107px;
    list-style: none;
  }
  .services li {
    display: flex;
    align-items: center;
    gap: 9px;
    height: 27.5px;
    font-size: 12.5px;
    color: var(--ink);
  }
  .services li::before {
    content: "";
    width: 7px;
    height: 7px;
    background: var(--brand-blue);
    flex: none;
  }

  .footer-rule {
    position: absolute;
    left: 0; right: 0;
    top: 265px;
    height: 3px;
    background: var(--accent-orange);
  }
  .footer-band {
    position: absolute;
    left: 0; right: 0;
    top: 268px;
    height: 36px;
    background: var(--brand-blue);
    color: var(--band-text);
    font-size: 13px;
    display: flex;
    align-items: center;
    padding-left: 20px;
    white-space: nowrap;
  }
  .footer-band .sep { margin: 0 12px; }
  .footer-band strong { font-weight: 600; }
</style>
</head>
<body>
  <section class="card card--front">
    <div class="faint-square" aria-hidden="true"></div>
    <div class="brand">
      <div class="brand-square" aria-hidden="true"></div>
      <div class="brand-name">Vantora</div>
    </div>
    <div class="divider"></div>
    <h1 class="contact-name">Declan Whitfield</h1>
    <p class="contact-title">Title Goes Here</p>
    <ul class="services">
      <li>Electronic Security</li>
      <li>Alarm Systems</li>
      <li>CCTV</li>
      <li>Electronic Access Control</li>
      <li>Security System Integration</li>
    </ul>
    <div class="footer-rule"></div>
    <div class="footer-band">
      <span>PO Box 862 Carrowbrook Qld 4179</span>
      <span class="sep">|</span>
      <span><strong>Ph:</strong> 07 38265014</span>
      <span class="sep">|</span>
      <span><strong>Mob:</strong> 0428615937</span>
    </div>
  </section>

  <section class="card card--back">
    <div class="faint-square" aria-hidden="true"></div>
    <div class="brand">
      <div class="brand-square" aria-hidden="true"></div>
      <div class="brand-name">Vantora</div>
    </div>
  </section>
</body>
</html>
```